Diverse, up-scale salon needs eye-catching, unique business cards.

We are looking for a unique business card design for our stylist but that can also be multi functional and used for appointment reminder and referrals. I will need a design in a format that I can modify names and titles going forward. In the past we have had a dark background with the logo on one side, and stylist and contact information on the other but we are open to all ideas. I have included our mission statement as well as branded colors below. The statement doesn't need to go on the card, it's just a reference for target market. We need space for the stylists name, title, instagram handle and then the salons phone number, website and address. I am also open to adding a spot for a qr code linked to the stylist instagram or the salon booking link.

primary brand colors:
#333333 #233415 #36502a #93874a #000000
Mission statement:
Morvane Hair Studio, a high-end salon located in the lively Downtown Farmington, Michigan, is committed to providing exceptional services in a welcoming and relaxed environment to meet the needs of our diverse clientele.
Our salon specializes in contemporary custom haircuts, coloring, extensions, and barbering and beard grooming services. Our team of skilled stylists is passionate and inventive in their hair styling techniques. At the heart of our salon are values centered on quality, innovation, creativity, and above all, comfort. These core values are evident in every appointment across our customizable array of services.
Our goal is to establish a benchmark for exceptional hair care for every human.
Website: www.morvanehairstudio-demo.com
instagram: @morvanehairstudio
address: 41872 Pelton Brook Rd, Farmington MI
phone: 248-316-8847

Industry/Entity Type

Hair Salon

Contact Information for Business Card

Stylist name, title, phone, instagram, website, address, (optional qr code)

Requirements
Should not have
• Does not need mission statement on the card.

```html
<!DOCTYPE html>
<html lang="en">
<head>
<meta charset="utf-8">
<title>Morvane Hair Studio – Business Card</title>
<link href="https://fonts.googleapis.com/css2?family=Arimo:wght@400;700&display=swap" rel="stylesheet">
<style>
  :root {
    --backdrop: #1e1e1e;
    --gold: #93874a;
    --white: #ffffff;
    --font: "Arimo", Arial, sans-serif;
  }
  * { margin: 0; padding: 0; box-sizing: border-box; }
  html, body { width: 1200px; height: 1059px; overflow: hidden; }
  body { background: var(--backdrop); position: relative; font-family: var(--font); }

  .card { position: absolute; overflow: hidden; box-shadow: 0 8px 24px rgba(0,0,0,.6); }

  /* Front */
  .card-front { left: 258px; top: 89px; width: 689px; height: 393px; background: var(--white); }
  .front-brand { position: absolute; left: 0; top: 0; width: 100%; height: 235px;
    display: flex; flex-direction: column; align-items: center; justify-content: center; gap: 14px; }
  .brand-dot { width: 54px; height: 54px; border-radius: 50%; background: var(--gold); }
  .brand-name { font-weight: 700; font-size: 26px; letter-spacing: 3px; color: var(--gold); text-transform: uppercase; }
  .front-info { position: absolute; left: 0; top: 235px; width: 100%; height: 158px; background: var(--gold); color: var(--white); }
  .person { position: absolute; right: 405px; top: 36px; text-align: right; white-space: nowrap; }
  .person-name { font-weight: 700; font-size: 21px; line-height: 22px; }
  .person-title { font-size: 17px; line-height: 18px; }
  .divider { position: absolute; left: 300px; top: 18px; width: 1.5px; height: 74px; background: var(--white); }
  .contacts { position: absolute; left: 320px; top: 12px; list-style: none; }
  .contacts li { display: flex; align-items: center; height: 28.5px; font-size: 19px; white-space: nowrap; }
  .contacts svg { width: 16px; height: 16px; margin-right: 10px; flex: none; }
  .address { position: absolute; left: 0; width: 100%; top: 106px; text-align: center; font-size: 18px; }

  /* Back */
  .card-back { left: 252px; top: 540px; width: 701px; height: 400px; background: var(--gold); color: var(--white); }
  .back-brand { position: absolute; left: 0; top: 0; width: 100%; height: 315px;
    display: flex; flex-direction: column; align-items: center; justify-content: center; gap: 18px; }
  .back-brand .brand-dot { width: 70px; height: 70px; background: var(--white); }
  .back-brand .brand-name { color: var(--white); font-size: 32px; }
  .services-head { position: absolute; left: 48px; right: 48px; top: 320px; height: 24px; display: flex; align-items: center; }
  .services-head .rule { flex: 1; height: 1.5px; background: var(--white); }
  .services-pill { margin: 0 7px; padding: 2px 9px; background: var(--white); color: var(--gold);
    border-radius: 14px; font-weight: 700; font-size: 19px; line-height: 21px; }
  .services-list { position: absolute; left: 0; width: 100%; top: 353px; text-align: center; font-size: 17.5px; white-space: nowrap; }
  .services-list span::before { content: ""; display: inline-block; width: 7px; height: 7px; border-radius: 50%;
    background: var(--white); margin: 0 4px 2px 5px; vertical-align: middle; }
</style>
</head>
<body>
  <section class="card card-front">
    <div class="front-brand">
      <div class="brand-dot"></div>
      <div class="brand-name">Morvane Hair Studio</div>
    </div>
    <div class="front-info">
      <div class="person">
        <div class="person-name">DANIEL REYES</div>
        <div class="person-title">Manager</div>
      </div>
      <div class="divider"></div>
      <ul class="contacts">
        <li>
          <svg viewBox="0 0 16 16" fill="none" stroke="#fff" stroke-width="1.5" stroke-linecap="round">
            <path d="M4 2 L6 5 L5 6.5 Q6.5 9.5 9.5 11 L11 10 L14 12 L12.5 14 Q6 13.5 2 4 Z"/>
            <path d="M9.5 2.5 Q13 3 13.5 6.5"/><path d="M9.5 5 Q11 5.2 11.2 6.8"/>
          </svg>248-316-8847
        </li>
        <li>
          <svg viewBox="0 0 16 16" fill="none" stroke="#fff" stroke-width="1.6">
            <circle cx="8" cy="8" r="6.2"/>
          </svg>@morvanehairstudio
        </li>
        <li>
          <svg viewBox="0 0 16 16" fill="none" stroke="#fff" stroke-width="1.2">
            <circle cx="8" cy="8" r="6.5"/><ellipse cx="8" cy="8" rx="3" ry="6.5"/>
            <line x1="1.5" y1="8" x2="14.5" y2="8"/><line x1="2.5" y1="4.8" x2="13.5" y2="4.8"/><line x1="2.5" y1="11.2" x2="13.5" y2="11.2"/>
          </svg>www.morvanehairstudio-demo.com
        </li>
      </ul>
      <div class="address">41872 Pelton Brook Rd, Farmington MI</div>
    </div>
  </section>

  <section class="card card-back">
    <div class="back-brand">
      <div class="brand-dot"></div>
      <div class="brand-name">Morvane Hair Studio</div>
    </div>
    <div class="services-head">
      <div class="rule"></div>
      <div class="services-pill">OUR SERVICES</div>
      <div class="rule"></div>
    </div>
    <div class="services-list">
      <span>Custom Haircuts</span><span>Coloring</span><span>Extensions</span><span>And Barbering</span><span>Beard Grooming</span>
    </div>
  </section>
</body>
</html>
```